Private Dining Restaurant Menu Design

Looking for help in designing a private dining room menu brochure - probably would need 4 panel layout to make all of the content fit, or a 5.5x8" booklet. Open to your ideas on layout/vessel - would want to post on website and be able to print to hand out to guests interested in booking our private dining room.

All content is in the attached "Private Dining Menu".

Would like to match existing dinner menu design - also attached.

Website is www.tallowfenkitchen.com

Requirements
Must have
• Easy to read format of a brochure of the private dining menu content - want to be able to hand out to interested guests and have it simple and easy to read/flip through.

```html
<!DOCTYPE html>
<html lang="en">
<head>
<meta charset="utf-8">
<title>Lunch Options — Private Dining Menu</title>
<link href="https://fonts.googleapis.com/css2?family=Barlow+Semi+Condensed:wght@500;700;800&family=Barlow:wght@400;500&display=swap" rel="stylesheet">
<style>
  :root {
    --paper: #f4f1ec;
    --paper-light: #fbfaf7;
    --red: #b03a32;
    --navy: #1f2d63;
    --rule: #b03a32;
    --photo-dark: #3b3029;
    --photo-mid: #7a6a5a;
    --photo-light: #c9bfb2;
  }
  * { margin: 0; padding: 0; box-sizing: border-box; }
  html, body { width: 825px; height: 1200px; overflow: hidden; }
  body {
    background: linear-gradient(100deg, var(--paper) 0%, var(--paper-light) 45%, var(--paper) 100%);
    font-family: "Barlow", sans-serif;
    color: var(--navy);
    position: relative;
  }
  .menu-page { position: absolute; left: 42px; width: 740px; top: 0; height: 1200px; }

  .page-title {
    position: absolute; top: 40px; left: 0; width: 740px;
    display: flex; align-items: center; gap: 14px;
    font-family: "Barlow Semi Condensed", sans-serif;
    font-weight: 800; font-size: 36px; letter-spacing: 1px;
    color: var(--red); text-transform: uppercase; line-height: 1;
  }
  .page-title::after, .option-title::after {
    content: ""; flex: 1; height: 2px; background: var(--rule);
  }
  .page-note {
    position: absolute; top: 80px; left: 0;
    font-family: "Barlow Semi Condensed", sans-serif;
    font-weight: 700; font-size: 22px; color: var(--red);
  }

  .option { position: absolute; left: 0; width: 740px; }
  .option-title {
    display: flex; align-items: center; gap: 14px;
    font-family: "Barlow Semi Condensed", sans-serif;
    font-weight: 700; font-size: 25px; letter-spacing: 0.5px;
    color: var(--red); text-transform: uppercase; line-height: 1;
  }
  .option-detail {
    margin-top: 9px;
    font-family: "Barlow Semi Condensed", sans-serif;
    font-weight: 700; font-size: 17.5px; color: var(--red);
  }
  .option-items { list-style: none; margin-top: 22px; }
  .option-items li {
    font-size: 17.5px; font-weight: 500; line-height: 21px;
    padding-left: 11px; position: relative;
  }
  .option-items li::before {
    content: "•"; position: absolute; left: 0;
  }
  .option-b .option-items li, .option-c .option-items li { line-height: 24px; }

  .option-a { top: 126px; }
  .option-b { top: 336px; }
  .option-c { top: 578px; }

  .closing-rule {
    position: absolute; top: 796px; left: 0; width: 738px; height: 2px;
    background: var(--rule);
  }
  .room-photo {
    position: absolute; top: 824px; left: 214px; width: 308px; height: 308px;
    background: linear-gradient(160deg, var(--photo-dark) 0%, var(--photo-mid) 45%, var(--photo-light) 100%);
  }
</style>
</head>
<body>
  <main class="menu-page">
    <h1 class="page-title">Lunch Options</h1>
    <p class="page-note">(an option must be chosen for groups of 15 or more, served before 3pm)</p>

    <section class="option option-a">
      <h2 class="option-title">Option A - $10-$12/Person</h2>
      <p class="option-detail">Pick Two Lunch Menu – Soup/Salad ($10), Soup/Sandwich ($11), or Salad/Sandwich ($12)</p>
      <ul class="option-items">
        <li>Sandwiches: ½ Turkey Club, ½ BLTA, BBQ Pork Sliders (2), Wood-Roasted Rotisserie Chicken<br>Sliders (2), Walleye Tacos (2), or Chicken Tacos (2)</li>
        <li>Soups: Chicken Wild Rice, White Chicken Chili, or Soup of the Day</li>
        <li>Salads: Wedge, House, or Caesar Salad</li>
      </ul>
    </section>

    <section class="option option-b">
      <h2 class="option-title">Option B - $13/Person</h2>
      <p class="option-detail">Served with your choice of fries, cheesy hashbrowns, soup, or apple cabbage slaw</p>
      <ul class="option-items">
        <li>Applewood Bacon &amp; Fajita Chicken Salad</li>
        <li>Rotisserie Chicken Salad</li>
        <li>Brown Sugar Bacon and Smoked Cheddar Burger</li>
        <li>Pepperjack Turkey Melt</li>
        <li>Walleye Fish Tacos</li>
      </ul>
    </section>

    <section class="option option-c">
      <h2 class="option-title">Option C - $13/Person Buffet Option</h2>
      <p class="option-detail">Food ready upon arrival, or at a set time of your choice</p>
      <ul class="option-items">
        <li>Sandwich platter – Assorted Rotisserie Turkey Club, Ham and Cheese, and Veggie Wrap</li>
        <li>Rotisserie Chicken Salad Bar</li>
        <li>Fresh Fruit Platter</li>
        <li>House-made Potato Chips</li>
      </ul>
    </section>

    <div class="closing-rule"></div>
    <div class="room-photo" role="img" aria-label="Photo of the private dining room with set tables, chairs and a stone fireplace"></div>
  </main>
</body>
</html>
```